Email mail merge - not a marketing email, this is an update email sent regularly to our members

HI I need a generic email designed to send out to our members, this is a tri-weekly (monday - updates - Wednesday - updates and Fridays - weekly round up.

we would like it to have within the mail body, 3 interactive, changeable boxes for example "quote of the week', 'top performer' and something else, It would be great if we can remove a box if and when we choose.
Our company is called Vr4lo Amusements or Vr4lo for short.
It needs to be in HTML to fit with our back office software.
We have all the logos for you already which I have included, I have also included our current email header.
our websites are...
vr4lam.cub - This is our members back end site.
vr4lam.com - This is our gaming site.
Please email me on derek@vr4lam.com if you have any queries

Target Market(s)

All of our members - We currently have over 400 but it is growing at an astronomical rate.

Industry/Entity Type

Marketing

Font styles to use
Serif
Decorative
Script

Requirements
Must have
• At least two interactive, changeable boxes/areas that I can put photo's or quotes in to. I would also like some guidelines as to how I change these myself.
• The colours should be inline with our vr4lam.club site.
Nice to have
• This is a positive email update so it needs to look clean and clear but vibrant, we are a unique company that is breaking records and is very successful.
• Our members have the ability and some already are earning vast sums of money.

```html
<!DOCTYPE html>
<html lang="en">
<head>
<meta charset="utf-8">
<title>Vr4lo Club Member Update</title>
<link rel="stylesheet" href="https://fonts.googleapis.com/css2?family=Jost:wght@400;500;600;700&family=Lora:wght@400&family=Arimo:ital,wght@0,400;0,700;1,700&display=swap">
<style>
  :root {
    --frame: #9aa3a1;
    --paper: #ffffff;
    --band: #f3f3f3;
    --teal-dark: #1e5a56;
    --teal-deep: #174643;
    --panel: #0f2428;
    --mint: #7ee0d8;
    --amber: #f7b216;
    --ink: #1c1c1c;
    --body: #333333;
    --muted: #999999;
    --logo: #8c9496;
    --rule: #cccccc;
  }
  * { margin: 0; padding: 0; box-sizing: border-box; }
  html, body { width: 1200px; height: 4412px; overflow: hidden; }
  body { background: var(--frame); font-family: "Arimo", Arial, sans-serif; color: var(--body); position: relative; }

  .browser-link { position: absolute; top: 28px; left: 0; width: 1200px; text-align: center; color: #fff; font-size: 23px; }

  .sheet { position: absolute; left: 44px; top: 82px; width: 1112px; height: 4286px; background: var(--paper); }
  .sheet > * { position: absolute; }

  .brand-logo { top: 95px; left: 0; width: 1112px; text-align: center; font-family: "Jost", sans-serif; font-weight: 700; font-size: 104px; letter-spacing: 2px; color: var(--logo); line-height: 1; }

  .hero-devices { top: 200px; left: 88px; width: 930px; height: 540px; border-radius: 10px;
    background: linear-gradient(160deg, #3a4244 0%, #1b2124 55%, #c9cfd1 100%); }

  .quote-band { top: 1028px; left: 0; width: 1112px; height: 305px; background: var(--band); }
  .quote-ribbon { top: 938px; left: 132px; width: 848px; height: 175px; }
  .quote-ribbon-title { top: 958px; left: 215px; width: 682px; text-align: center; color: #fff; font-family: "Jost", sans-serif; font-weight: 500; font-size: 52px; letter-spacing: 2px; }
  .quote-text { top: 1118px; left: 100px; width: 912px; text-align: center; font-family: "Lora", serif; font-size: 42px; line-height: 52px; color: var(--ink); }
  .quote-rule { top: 1270px; left: 450px; width: 132px; height: 6px; background: var(--teal-dark); }

  .performer-panel { top: 1333px; left: 0; width: 1112px; height: 535px; background: var(--panel); }
  .performer-photo { top: 1388px; left: 59px; width: 420px; height: 418px; border: 9px solid #5a6467;
    background: linear-gradient(180deg, #e6d5b3 0%, #d9b48e 50%, #f1eee9 100%); }
  .performer-title { top: 1372px; left: 529px; color: var(--mint); font-family: "Jost", sans-serif; font-weight: 500; font-size: 64px; letter-spacing: 1px; line-height: 1; }
  .performer-sub { top: 1450px; left: 529px; color: #fff; font-family: "Jost", sans-serif; font-weight: 500; font-size: 44px; line-height: 1; }
  .performer-name { top: 1515px; left: 531px; color: var(--amber); font-weight: 700; font-style: italic; font-size: 32px; }
  .performer-bio { top: 1578px; left: 529px; width: 540px; color: #fff; font-size: 26.5px; line-height: 41px; }

  .section-title { left: 0; width: 1112px; text-align: center; font-family: "Jost", sans-serif; font-weight: 600; font-size: 64px; color: var(--ink); line-height: 1; letter-spacing: 1px; }
  .section-sub { left: 0; width: 1112px; text-align: center; font-family: "Jost", sans-serif; font-weight: 500; font-size: 35px; color: #444; line-height: 1; letter-spacing: 1px; }
  .section-copy { left: 74px; width: 964px; text-align: center; font-size: 25px; line-height: 37px; color: var(--body); }
  .section-copy p + p { margin-top: 38px; }

  .cta { display: flex; align-items: center; justify-content: center; gap: 34px; background: var(--amber); border-radius: 50px; color: var(--ink); font-family: "Jost", sans-serif; font-weight: 500; font-size: 34px; text-decoration: none; }
  .cta-divider { width: 3px; height: 46px; background: var(--ink); }
  .cta svg { width: 42px; height: 42px; }

  .rule-dashed { left: 53px; width: 1006px; border-top: 3px dashed var(--rule); height: 0; }

  .office-title { top: 3773px; left: 56px; color: var(--muted); font-family: "Jost", sans-serif; font-weight: 500; font-size: 29px; letter-spacing: 3px; }
  .office-address { top: 3858px; left: 56px; width: 520px; color: var(--muted); font-size: 24.5px; line-height: 37px; font-style: normal; }
  .office-address .strong { color: #444; }
  .ent-logo { top: 3818px; left: 600px; width: 490px; text-align: center; font-family: "Jost", sans-serif; font-weight: 700; font-size: 76px; color: var(--logo); line-height: 1; }
  .social-row { top: 4148px; left: 0; width: 1112px; display: flex; justify-content: center; gap: 52px; }
  .social-row span { width: 28px; height: 28px; border-radius: 50%; background: #9a9a9a; }
</style>
</head>
<body>
  <div class="browser-link">View this mail in web browser</div>

  <main class="sheet">
    <div class="brand-logo">VR4LO CLUB</div>
    <div class="hero-devices" role="img" aria-label="Laptop, tablet and phone showing the members gaming site"></div>

    <div class="quote-band"></div>
    <svg class="quote-ribbon" viewBox="0 0 848 175" aria-hidden="true">
      <polygon points="0,40 130,40 130,175 0,175 38,108" fill="var(--teal-deep)"/>
      <polygon points="848,40 718,40 718,175 848,175 810,108" fill="var(--teal-deep)"/>
      <polygon points="83,91 127,91 127,130" fill="#0c2e2c"/>
      <polygon points="765,91 721,91 721,130" fill="#0c2e2c"/>
      <rect x="83" y="0" width="682" height="91" fill="var(--teal-dark)"/>
    </svg>
    <h2 class="quote-ribbon-title">QUOTE OF THE WEEK</h2>
    <blockquote class="quote-text">Lorem isum dolosr sit amet esta di maria nuno valencia ed di mordor.</blockquote>
    <div class="quote-rule"></div>

    <section class="performer-panel"></section>
    <div class="performer-photo" role="img" aria-label="Portrait photo of this week's top performer"></div>
    <h2 class="performer-title">TOP PERFORMER</h2>
    <div class="performer-sub">OF THE WEEK</div>
    <div class="performer-name">Marisol Quenby</div>
    <p class="performer-bio">Nulla vestibulum mauris ac est consequat, quis dapibus diam porta. Suspendisse non ligula lacinia nisi interdum vulputate in sed purus. Quisque eget felis non libero euismod ultricies tristique at nibh.</p>

    <h2 class="section-title" style="top:1926px">LATEST NEWS</h2>
    <div class="section-sub" style="top:2002px">THIS WEEK'S NEWS</div>
    <div class="section-copy" style="top:2112px">
      <p>Join the VR4LO CLUB Membership and Rewards Program today to start earning income with a new dedicated Gaming and Sport Betting Service directed to the networking industry.</p>
      <p>VR4LO CLUB caters to all levels of users with its range of six rewarding membership plans:, Bronze, Silver, Gold, Ruby, Emerald and Diamond Founder, The Diamond Founder plan is much sought after because there are barely one hundred such memberships on offer worldwide. Nonetheless, each of these plans is a package of delights: earn commissions, share your moneymaking adventure at VR4LO CLUB throughout the membership lifetime, and carry no liability of negative monthly spillovers. It's like you sign a fun contract once you choose us!</p>
    </div>
    <a class="cta" href="#" style="top:2623px;left:309px;width:485px;height:88px">SEE MORE NEWS <span class="cta-divider"></span>
      <svg viewBox="0 0 42 42" aria-hidden="true"><circle cx="21" cy="21" r="18" fill="none" stroke="var(--ink)" stroke-width="4"/><path d="M12 21h16M21 13l8 8-8 8" fill="none" stroke="var(--ink)" stroke-width="4"/></svg></a>

    <h2 class="section-title" style="top:2812px">WEEKLY UPDATES</h2>
    <div class="section-sub" style="top:2888px">CHECK LATEST UPDATES</div>
    <div class="section-copy" style="top:2998px">
      <p>Join the VR4LO CLUB Membership and Rewards Program today to start earning income with a new dedicated Gaming and Sport Betting Service directed to the networking industry.</p>
      <p>VR4LO CLUB caters to all levels of users with its range of six rewarding membership plans:, Bronze, Silver, Gold, Ruby, Emerald and Diamond Founder, The Diamond Founder plan is much sought after because there are barely one hundred such memberships on offer worldwide. Nonetheless, each of these plans is a package of delights: earn commissions, share your moneymaking adventure at VR4LO CLUB throughout the membership lifetime, and carry no liability of negative monthly spillovers. It's like you sign a fun contract once you choose us!</p>
    </div>
    <a class="cta" href="#" style="top:3506px;left:274px;width:556px;height:90px">SEE MORE UPDTAES <span class="cta-divider"></span>
      <svg viewBox="0 0 42 42" aria-hidden="true"><circle cx="21" cy="21" r="18" fill="none" stroke="var(--ink)" stroke-width="4"/><path d="M12 21h16M21 13l8 8-8 8" fill="none" stroke="var(--ink)" stroke-width="4"/></svg></a>

    <div class="rule-dashed" style="top:3712px"></div>
    <div class="office-title">REGISTERED OFFICES</div>
    <address class="office-address">Suite 4, Harbour Court Quay Road, Port Elms, Coastal Territory on the southern shore<br><span class="strong">Ph:</span>1300 555 019<br>Email: <span class="strong">support@vr4lam.com</span></address>
    <div class="ent-logo">VR4LO ENT</div>
    <a class="cta" href="#" style="top:3932px;left:574px;width:491px;height:73px;font-size:27px;gap:26px">VISIT OUR GAMING WEBSITE <span class="cta-divider" style="height:38px"></span>
      <svg viewBox="0 0 42 42" style="width:34px;height:34px" aria-hidden="true"><circle cx="21" cy="21" r="18" fill="none" stroke="var(--ink)" stroke-width="4"/><path d="M12 21h16M21 13l8 8-8 8" fill="none" stroke="var(--ink)" stroke-width="4"/></svg></a>
    <div class="rule-dashed" style="top:4094px"></div>
    <nav class="social-row" aria-label="Social links"><span></span><span></span><span></span><span></span><span></span></nav>
  </main>
</body>
</html>
```